Fenwick Quarter Summer Party Invitation

We need an invitation to be designed for our annual summer party for Fenwick Quarter in Chelsea, London. The area has a relaxed family atmosphere but is on the edge of the bustle of Chelsea. The committee has specified the following:

TO INCLUDE THE FOLLOWING INFORMATION - will it be the same two sided format as last year? Maybe the reverse can use your pale blue and your London skyline "logo"

Should the following, highlighted in blue, be very bold on the front of the invite? With the Harlow & Pike sales and lettings logo.
SUMMER PARTY 2016
Fenwick Quarter Chelsea is holding a Summer Party to celebrate the Duke's 90th Birthday

Date: Saturday 18th June 2016
Time: 2.00pm to 5.00pm
Place: Brimble Lane South (the pedestrianised section off Ockenden Street) MAP?

Open to all residents of Fenwick Quarter and admittance is by invitation only.
Please keep this invitation safe and bring it with you on the day

Then more detail on the rear:

Fenwick Quarter Chelsea
Formerly known as Dunmere Residents' Association of Fenwick Quarter

Email: dunmerera@postbox-mail.test
Website: dunmerera-example.co.uk
OUR TYPEFACE IS ARIAL. The rest can be in any typeface but Arial is our "logo"

Dress code: red white and blue (or black ) as simple or elaborate as you like Live Music Children's entertainment and activities Food Drinks Tea and cakes

SPONSORS:
Harlow & Pike. Ensuring this is prominent as the main sponsor Kestrel Arms
412 Blues club etc etc
Larkfield Yard Studios
List to follow.............

Space needs to be left on the rear for sponsors details to be added. They would like something with an almost retro, traditional British feel.
Our Harlow & Pike logo attached and branding.

Also a flyer that association seemed to like.

I would suggest postcard (A6 sized) or maybe A5 at the biggest

Target Market(s)

Local Residents

Colors
ec1f27
ffffff
0355a3

Requirements
Must have
• Information on the description

```html
<!DOCTYPE html>
<html lang="en">
<head>
<meta charset="utf-8">
<title>Fenwick Quarter Summer Party Invitation</title>
<link href="https://fonts.googleapis.com/css2?family=Bebas+Neue&family=Chivo:ital,wght@0,400;0,700;1,400;1,700&display=swap" rel="stylesheet">
<style>
  :root {
    --navy: #0c2b5e;
    --red: #d3202b;
    --white: #ffffff;
    --teal: #0f6e8d;
    --brand-teal: #1b78a6;
    --badge: #6b3a7a;
    --bg-light: #1190cf;
    --bg-dark: #0a6ba5;
  }
  * { margin: 0; padding: 0; box-sizing: border-box; }
  html, body { width: 1200px; height: 1000px; overflow: hidden; }
  body {
    position: relative;
    background: radial-gradient(ellipse at 35% 40%, var(--bg-light), var(--bg-dark));
    font-family: "Chivo", Arial, sans-serif;
    color: var(--navy);
  }
  .card {
    position: absolute;
    top: 170px;
    width: 472px;
    height: 660px;
    box-shadow: 0 10px 24px rgba(0, 0, 0, 0.35);
  }
  .card--front { left: 94px; }
  .card--back { left: 633px; }
  .card__flag { position: absolute; inset: 0; display: block; }
  .card__panel {
    position: absolute;
    left: 34px; top: 33px; right: 34px; bottom: 33px;
    background: var(--white);
    text-align: center;
    overflow: hidden;
  }
  .title {
    position: absolute; left: 0; right: 0; top: 14px;
    font-family: "Bebas Neue", "Arial Narrow", sans-serif;
    font-weight: 400; font-size: 55px; letter-spacing: 0.5px;
    line-height: 1; white-space: nowrap;
  }
  .sponsor-mark {
    position: absolute; right: 46px; top: 66px; text-align: right;
    color: var(--brand-teal); font-weight: 700; line-height: 1;
  }
  .sponsor-mark__name { font-size: 14px; }
  .sponsor-mark__tag { font-size: 8px; font-weight: 700; margin-top: 2px; }
  .celebration-badge {
    position: absolute; left: 150px; top: 100px; width: 104px; height: 112px;
  }
  .front-text {
    position: absolute; left: 0; right: 0; font-weight: 700; font-size: 12.5px; line-height: 16px;
  }
  .front-text--intro { top: 244px; }
  .front-text--when { top: 321px; font-style: italic; }
  .front-text--notes { top: 392px; font-style: italic; }
  .front-text--notes p + p { margin-top: 14px; }
  .front-text--place { top: 506px; font-size: 14px; line-height: 18px; font-style: normal; }

  .back-heading { position: absolute; left: 0; right: 0; top: 19px; font-weight: 700; font-size: 18px; }
  .back-former { position: absolute; left: 0; right: 0; top: 42px; font-style: italic; font-size: 14px; line-height: 18px; }
  .back-details { position: absolute; left: 0; right: 0; top: 108px; font-weight: 700; font-size: 13.5px; line-height: 18px; }
  .back-menu { position: absolute; left: 0; right: 0; top: 182px; font-weight: 700; font-size: 19px; color: var(--red); }
  .back-menu span { color: var(--navy); font-size: 14px; margin: 0 3px; }
  .back-sponsors-label { position: absolute; left: 0; right: 0; top: 253px; font-weight: 700; font-size: 17px; }
  .back-sponsors { position: absolute; left: 0; right: 0; top: 275px; font-style: italic; font-weight: 700; font-size: 14px; }
  .skyline {
    position: absolute; left: 0; right: 0; top: 495px; height: 30px;
    background: linear-gradient(to bottom, rgba(15,110,141,0.15), rgba(15,110,141,0.85));
  }
  .contact {
    position: absolute; left: 0; right: 0; bottom: 0; height: 69px;
    background: var(--teal); color: var(--white);
    font-weight: 700; font-size: 14px; line-height: 18px; padding-top: 19px;
  }
</style>
</head>
<body>
  <section class="card card--front">
    <svg class="card__flag" viewBox="0 0 472 660" aria-hidden="true">
      <rect width="472" height="660" fill="var(--navy)"/>
      <path d="M0 0L472 660M472 0L0 660" stroke="var(--white)" stroke-width="70"/>
      <path d="M0 0L472 660M472 0L0 660" stroke="var(--red)" stroke-width="24"/>
      <rect x="157" width="158" height="660" fill="var(--white)"/>
      <rect y="276" width="472" height="109" fill="var(--white)"/>
      <rect x="189" width="94" height="660" fill="var(--red)"/>
      <rect y="298" width="472" height="65" fill="var(--red)"/>
      <rect x="24" y="23" width="424" height="614" fill="var(--navy)"/>
    </svg>
    <div class="card__panel">
      <h1 class="title">SUMMER PARTY 2016</h1>
      <div class="sponsor-mark">
        <div class="sponsor-mark__name">HARLOW &amp; PIKE</div>
        <div class="sponsor-mark__tag">Sales &amp; Lettings</div>
      </div>
      <svg class="celebration-badge" viewBox="0 0 104 112" role="img" aria-label="Celebration badge for the Duke's 90th birthday">
        <circle cx="52" cy="36" r="34" fill="var(--badge)"/>
        <rect x="8" y="78" width="88" height="32" rx="4" fill="var(--badge)" opacity="0.35"/>
      </svg>
      <div class="front-text front-text--intro">
        SUMMER PARTY 2016<br>Fenwick Quarter Chelsea is holding<br>a Summer Party to celebrate<br>the Duke's 90th Birthday
      </div>
      <div class="front-text front-text--when">
        Date: Saturday 18th June 2016<br>Time: 2.00pm to 5.00pm
      </div>
      <div class="front-text front-text--notes">
        <p>* Open to all residents of Fenwick Quarter<br>admittance is by invitation only</p>
        <p>* Please keep this invitation safe<br>and bring it with you on the day</p>
      </div>
      <div class="front-text front-text--place">
        Place:<br>Brimble Lane South<br>(the pedestrianised section off Ockenden Street)
      </div>
    </div>
  </section>

  <section class="card card--back">
    <svg class="card__flag" viewBox="0 0 472 660" aria-hidden="true">
      <rect width="472" height="660" fill="var(--navy)"/>
      <path d="M0 0L472 660M472 0L0 660" stroke="var(--white)" stroke-width="70"/>
      <path d="M0 0L472 660M472 0L0 660" stroke="var(--red)" stroke-width="24"/>
      <rect x="157" width="158" height="660" fill="var(--white)"/>
      <rect y="276" width="472" height="109" fill="var(--white)"/>
      <rect x="189" width="94" height="660" fill="var(--red)"/>
      <rect y="298" width="472" height="65" fill="var(--red)"/>
      <rect x="24" y="23" width="424" height="614" fill="var(--navy)"/>
    </svg>
    <div class="card__panel">
      <h2 class="back-heading">Fenwick Quarter Chelsea</h2>
      <p class="back-former">Formerly known as<br>Dunmere Residents' Association of Fenwick Quarter</p>
      <p class="back-details">Dress code: red white and blue (or black )<br>as simple or elaborate as you like<br>Live Music Children's entertainment and activities</p>
      <p class="back-menu">Food <span>&bull;</span> Drinks <span>&bull;</span> Tea <span>&bull;</span> cakes</p>
      <h3 class="back-sponsors-label">SPONSORS:</h3>
      <p class="back-sponsors">Harlow &amp; Pike, 412 Blues Club, Larkfield Yard Studios</p>
      <div class="skyline" role="img" aria-label="London skyline silhouette"></div>
      <div class="contact">
        Email: dunmerera@postbox-mail.test<br>Website: www.dunmerera-example.co.uk
      </div>
    </div>
  </section>
</body>
</html>
```